Flyer für mobile tierärztliche Ultraschalluntersuchungen
Super Zusammenarbeit! Gerne wieder. Das war gerade schon das 2. Mal.
Zielgruppe
Mobile tierärztliche Ultraschalluntersuchungen, Zielgruppe: Tierärzt/Tierpraxen, die kein ultraschall Gerät od US-Kenntnisse haben.
Aufgabenstellung
1 Seite (recto D, verso F Sprache), professionell , seriös, aber optisch auffällig, damit es nicht direkt in Papierkorb landet.

```html
<!DOCTYPE html>
<html lang="fr">
<head>
<meta charset="utf-8">
<title>Flyer – échographie vétérinaire mobile</title>
<link rel="stylesheet" href="https://fonts.googleapis.com/css2?family=Barlow+Condensed:wght@400;500&display=swap">
<style>
  :root{
    --green:#76b45b;
    --green-light:#9cca84;
    --green-head:#5ea043;
    --green-dark:#3f6b35;
    --text-dark:#2f4a26;
    --white:#ffffff;
    --page:#ececec;
    --photo-a:#c9cbce;
    --photo-b:#5b6d8f;
    --photo-c:#c98d4f;
  }
  *{margin:0;padding:0;box-sizing:border-box}
  html,body{width:839px;height:1200px;overflow:hidden;background:var(--page)}
  body{font-family:"Barlow Condensed",sans-serif;position:relative}
  .spread{position:absolute;left:0;width:839px;height:279px;overflow:hidden;box-shadow:0 6px 12px rgba(0,0,0,.12)}
  .spread--fr{top:306px}
  .spread--de{top:606px}
  .panel{position:absolute;top:0;height:279px;width:280px;overflow:hidden}
  .panel--cover{left:0;background:var(--green)}
  .panel--service{left:280px;background:var(--white);width:279px}
  .panel--about{left:559px;background:var(--green)}
  .cover-photo{position:absolute;left:0;top:0;width:280px;height:186px;
    background:linear-gradient(135deg,var(--photo-a) 0%,#9aa1ab 40%,var(--photo-b) 60%,var(--photo-c) 85%)}
  .cover-photo--tinted{height:279px;opacity:.35}
  .brand-circle{position:absolute;left:200px;top:198px;width:62px;height:62px;border-radius:50%;background:var(--green-light)}
  .brand-name{position:absolute;left:18px;top:212px;font-size:17px;font-weight:400;color:var(--green-dark);white-space:nowrap}
  .rule{position:absolute;left:16px;right:0;top:263px;height:1.5px;background:var(--green-dark)}
  .service-title{position:absolute;top:30px;font-size:12px;font-weight:500;color:var(--green-head);white-space:nowrap;letter-spacing:.1px}
  .service-list{position:absolute;list-style:none;font-size:7px;line-height:10px;color:var(--text-dark);font-weight:500}
  .service-list li{margin-bottom:8.5px}
  .spread--fr .service-title{left:20px}
  .spread--fr .service-list{left:20px;top:59px;width:230px}
  .spread--de .service-title{right:16px}
  .spread--de .service-list{right:16px;top:55px;width:230px;text-align:right}
  .service-photo{position:absolute;border-radius:50%;
    background:radial-gradient(circle at 60% 55%,var(--photo-c) 0%,#8a7a66 25%,var(--photo-b) 50%,#d9dbde 80%)}
  .spread--fr .service-photo{left:123px;top:97px;width:184px;height:184px}
  .spread--de .service-photo{left:-30px;top:97px;width:180px;height:180px}
  .about-list{position:absolute;left:27px;top:34px;list-style:none;font-size:7.6px;line-height:11px;color:var(--white)}
  .about-list li{margin-bottom:9px}
  .probe{position:absolute;left:217px;top:0}
  .about-title{position:absolute;left:200px;top:96px;width:60px;text-align:center;font-size:12px;line-height:15px;color:var(--green-dark)}
  .contact{position:absolute;left:27px;top:169px;color:var(--green-dark)}
  .contact-head{font-size:11.5px;line-height:14px}
  .contact-sub{font-size:9px;line-height:14px;margin-bottom:6px}
  .contact-line{font-size:7.2px;line-height:10.5px}
  .portrait{position:absolute;left:154px;top:155px;width:146px;height:146px;border-radius:50%;
    background:radial-gradient(circle at 50% 40%,#c9a88a 0%,#6b5b52 35%,#2f3f6b 65%,#8c8b85 90%)}
</style>
</head>
<body>

<section class="spread spread--fr" lang="fr">
  <div class="panel panel--cover">
    <div class="cover-photo" role="img" aria-label="Photo : vétérinaire réalisant une échographie sur un chien couché"></div>
    <div class="brand-circle"></div>
    <div class="brand-name">Dr. med. vet. Lena Forsell</div>
  </div>
  <div class="panel panel--service">
    <div class="service-photo" role="img" aria-label="Photo circulaire : examen échographique d'un chien debout sur la table"></div>
    <h2 class="service-title">SERVICE ITINÉRANT D'ECHOGRAPHIE VÉTÉRINAIRE</h2>
    <ul class="service-list">
      <li>Je me déplace avec mon échographe de haute qualité Sonora Flex pour des échographies abdominales et thoraciques à votre cabinet</li>
      <li style="width:150px">Vos clients restent chez vous, pas de route en plus et la facturation se fait par votre cabinet</li>
      <li style="width:115px">Je m'occupe des chiens et de chats, mais aussi des NACs, y.c. les reptiles</li>
      <li style="width:90px">La prise de rendez-vous est flexible et rapide par email ou téléphone</li>
      <li style="width:90px">Nous pouvons échanger pour optimiser la prise en charge de vos patients</li>
      <li style="width:95px">Je parle quatre langues et les rapports peuvent se faire en français, allemand ou anglais</li>
    </ul>
  </div>
  <div class="panel panel--about">
    <ul class="about-list">
      <li>Diplômée de l'Université d'Aarwil en 2007</li>
      <li>Doctorat en pathologie de la faune sauvage</li>
      <li>Ayant plus de 10 ans de pratique clinique<br>(animaux de compagnie et NACs)</li>
      <li>Suivant des formations continues en échographie<br>en Suisse et à l'étranger</li>
    </ul>
    <svg class="probe" width="20" height="82" viewBox="0 0 20 82" aria-hidden="true">
      <line x1="10" y1="0" x2="10" y2="48" stroke="#3f6b35" stroke-width="1"/>
      <circle cx="10" cy="58" r="9" fill="none" stroke="#3f6b35" stroke-width="1"/>
    </svg>
    <div class="about-title">A PROPOS<br>DE MOI</div>
    <div class="contact">
      <div class="contact-head">Vous êtes curieux?</div>
      <div class="contact-sub">Rencontrons-nous pour discuter!</div>
      <div class="contact-line">Tél : +41 79 000 12 34</div>
      <div class="contact-line">Email: lforsell.vet@example.ch</div>
      <div class="contact-line">www.vetsono-mobil.ch</div>
    </div>
    <div class="portrait" role="img" aria-label="Photo portrait de la vétérinaire"></div>
  </div>
  <div class="rule"></div>
</section>

<section class="spread spread--de" lang="de">
  <div class="panel panel--cover">
    <div class="cover-photo cover-photo--tinted" role="img" aria-label="Grün getöntes Foto: Tierärztin bei einer Ultraschalluntersuchung"></div>
    <div class="brand-circle"></div>
    <div class="brand-name">Dr. med. vet. Lena Forsell</div>
  </div>
  <div class="panel panel--service">
    <div class="service-photo" role="img" aria-label="Rundes Foto: Ultraschalluntersuchung an einem stehenden Hund"></div>
    <h2 class="service-title">MOBILE TIERÄRZTLICHE SONOGRAPHIE</h2>
    <ul class="service-list">
      <li style="margin-left:-20px;width:250px">Ich komme mit meinen neuen hochqualitativen Gerät Sonora Flex für Abdomen- und Thorax Ultraschalluntersuchungen zu Ihnen, in Ihre Praxis</li>
      <li>Ihre Kunden bleiben bei Ihnen, haben keine Extra-Fahrten<br>und die Abrechnung findet über Ihrer Praxis statt</li>
      <li>Ich kümmere mich um Hunde und Katzen,<br>aber auch um Heimtiere, inkl. Reptilien</li>
      <li>Die Terminvereinbarung ist schnell<br>und flexibel per Email oder Telefon</li>
      <li>Wir können zusammen Kenntnisse<br>austauschen, um die Betreuung<br>Ihrer Patienten zu optimieren</li>
      <li>Ich spreche vier Sprachen und<br>kann Berichte auf Französisch,<br>Deutsch oder Englisch schreiben</li>
    </ul>
  </div>
  <div class="panel panel--about">
    <ul class="about-list">
      <li>Diplom in 2007 an der Universität Aarwil</li>
      <li>Doktor in Wildtierpathologie</li>
      <li>Seit über 10 Jahren klinisch bei Kleintieren und<br>Heimtieren tätig</li>
      <li>Konstante Weiterbildungen in der Schweiz<br>&amp; im Ausland</li>
    </ul>
    <svg class="probe" width="20" height="82" viewBox="0 0 20 82" aria-hidden="true">
      <line x1="10" y1="0" x2="10" y2="48" stroke="#3f6b35" stroke-width="1"/>
      <circle cx="10" cy="58" r="9" fill="none" stroke="#3f6b35" stroke-width="1"/>
    </svg>
    <div class="about-title">ÜBER<br>MICH</div>
    <div class="contact">
      <div class="contact-head">Sind Sie neugierig geworden?</div>
      <div class="contact-sub">Treffen wir uns, um uns kennenzulernen!</div>
      <div class="contact-line">Tel : +41 79 000 12 34</div>
      <div class="contact-line">Email: lforsell.vet@example.ch</div>
      <div class="contact-line">www.vetsono-mobil.ch</div>
    </div>
    <div class="portrait" role="img" aria-label="Porträtfoto der Tierärztin"></div>
  </div>
  <div class="rule"></div>
</section>

</body>
</html>
```